Ridgeline Outfitters Business Cards

Recently had a logo done with Artfolio and now looking for a business card to go along with it.

Target Market(s)

Ridgeline Outfitters is a weapons dealer. My market will be primarily men, hunting, shooting type.

Industry/Entity Type

Business

Contact Information for Business Card

I selected double sided, but this is not required, single or double is going to be fine. I picture the logo on one side, or perhaps just the circle which contains "RO" with the remaining info on the other side.

Font styles to use
Sans Serif

Requirements
Must have
• My name: Milo Brandt
• Title: Owner
• tel: 612-555-0187
• web: www.ridgelineoutfittersmn.example
Nice to have
• I like the concept of a black business card. I would like to keep the colors monotone, black, grey, white or red. Red is acceptable because it is in the logo. I have also seen cards that are matte black with shiny black as well, perhaps for the logo (or circle RO) part of the logo.
• I will upload a couple of the logos for use, and also an example I just found of the black on black. and some others that have a nice contrast.
Should not have
• lots of colors are not wanted.

```html
<!DOCTYPE html>
<html lang="en">
<head>
<meta charset="utf-8">
<title>Ridgeline Outfitters – Business Cards</title>
<link href="https://fonts.googleapis.com/css2?family=Lato:wght@400;700;900&display=swap" rel="stylesheet">
<style>
  :root {
    --page-bg: #d4d4d4;
    --band-grey: #a4a4a4;
    --card-dark: #2e2e30;
    --card-back: #2a2a2c;
    --logo-panel: #1f1f20;
    --logo-black: #050505;
    --accent-red: #e0161d;
    --mark-ink: #c8c8c8;
    --ink-dark: #2f2f31;
    --ink-light: #ffffff;
  }
  * { margin: 0; padding: 0; box-sizing: border-box; }
  html, body { width: 1200px; height: 750px; overflow: hidden; }
  body {
    background: var(--page-bg);
    position: relative;
    font-family: "Lato", Arial, sans-serif;
  }
  .card {
    position: absolute;
    left: 357px;
    width: 508px;
    height: 305px;
    overflow: hidden;
  }
  /* Front */
  .card--front { top: 58px; background: var(--card-dark); }
  .front-band {
    position: absolute; left: 0; top: 0; width: 100%; height: 112px;
    background: var(--band-grey);
    border-bottom: 3px solid var(--accent-red);
  }
  .wordmark {
    position: absolute; white-space: nowrap; letter-spacing: -0.5px;
  }
  .wordmark strong { font-weight: 900; }
  .wordmark span { font-weight: 400; }
  .front-band .wordmark {
    left: 33px; top: 36px; font-size: 29px; color: var(--ink-dark);
  }
  .logo-panel {
    position: absolute; left: 33px; top: 146px; width: 210px; height: 113px;
    background: var(--logo-panel);
    display: flex; align-items: center; justify-content: center;
  }
  .logo-name {
    font-weight: 700; color: var(--mark-ink); text-align: center;
    letter-spacing: 1px; line-height: 1.25;
  }
  .logo-panel .logo-name { font-size: 16px; }
  .contact {
    position: absolute; left: 258px; top: 143px; width: 220px; color: var(--ink-light);
  }
  .contact-name { font-size: 18px; line-height: 20px; white-space: nowrap; }
  .contact-name strong { font-weight: 700; }
  .contact-name span { font-weight: 400; }
  .contact-title { font-size: 13.5px; line-height: 14px; font-weight: 400; }
  .contact-rule { height: 1px; background: var(--ink-light); width: 198px; margin: 7px 0 10px; }
  .contact-list { list-style: none; }
  .contact-list li {
    display: flex; align-items: center; gap: 9px;
    font-size: 10.5px; line-height: 19px; white-space: nowrap;
  }
  .contact-list svg { width: 9px; height: 9px; flex: none; fill: var(--ink-light); }
  /* Back */
  .card--back { top: 395px; background: var(--card-back); }
  .back-logo {
    position: absolute; left: 168px; top: 18px; width: 182px; height: 182px;
    background: var(--logo-black);
    display: flex; align-items: center; justify-content: center;
  }
  .back-logo .logo-name { font-size: 19px; }
  .card--back .wordmark {
    left: 0; width: 100%; text-align: center; top: 214px;
    font-size: 26px; color: var(--ink-light);
  }
  .back-bar {
    position: absolute; left: 51px; top: 247px; width: 405px; height: 6px;
    background: var(--accent-red);
  }
</style>
</head>
<body>

<section class="card card--front" aria-label="Business card front">
  <div class="front-band">
    <h1 class="wordmark"><strong>RIDGELINE</strong> <span>OUTFITTERS</span></h1>
  </div>
  <div class="logo-panel">
    <p class="logo-name">RIDGELINE<br>OUTFITTERS</p>
  </div>
  <div class="contact">
    <p class="contact-name"><strong>Milo</strong> <span>BRANDT</span></p>
    <p class="contact-title">Owner</p>
    <div class="contact-rule"></div>
    <ul class="contact-list">
      <li>
        <svg viewBox="0 0 10 10" aria-hidden="true"><path d="M0 4 Q5 0 10 4 L8 5 L7 3.5 Q5 3 3 3.5 L2 5 Z M2 6 H8 L9 9 H1 Z"/></svg>
        612-555-0187
      </li>
      <li>
        <svg viewBox="0 0 10 10" aria-hidden="true"><path d="M0 2 H10 V8 H0 Z M0.8 2.6 L5 5.6 L9.2 2.6 V7.4 H0.8 Z" fill-rule="evenodd"/></svg>
        info@ridgelineoutfittersmn.example
      </li>
      <li>
        <svg viewBox="0 0 10 10" aria-hidden="true"><path d="M5 0.5 A4.5 4.5 0 1 0 5.01 0.5 Z M5 1.4 A3.6 3.6 0 1 1 4.99 1.4 Z M4.6 1 H5.4 V9 H4.6 Z M1 4.6 H9 V5.4 H1 Z" fill-rule="evenodd"/></svg>
        www.ridgelineoutfittersmn.example
      </li>
      <li>
        <svg viewBox="0 0 10 10" aria-hidden="true"><path d="M5 0 A3.5 3.5 0 0 1 8.5 3.5 C8.5 6 5 10 5 10 C5 10 1.5 6 1.5 3.5 A3.5 3.5 0 0 1 5 0 Z M5 2.2 A1.3 1.3 0 1 0 5.01 2.2 Z" fill-rule="evenodd"/></svg>
        Cedar Hollow, Minnesota
      </li>
    </ul>
  </div>
</section>

<section class="card card--back" aria-label="Business card back">
  <div class="back-logo">
    <p class="logo-name">RIDGELINE<br>OUTFITTERS</p>
  </div>
  <h2 class="wordmark"><strong>RIDGELINE</strong> <span>OUTFITTERS</span></h2>
  <div class="back-bar"></div>
</section>

</body>
</html>
```